Presentation Template for Copperline Ventures

We would like to have a template for our presentations since we have a new logo and want a new general image.

The new template should have as minimum Cover/Title Page, Bullets page and Regular page. We have a new logo and need the template to mach with it. For the bullets and regular page we want the design no take much part for including content, so we would like something that makes the slides look good but leaving most of room free for writing.

We would like the logo on the footer of the regular slides (not of course for the cover, dividers etc)

I'm attaching de logo here. Our logo colours are #b80016, #006ac6 and black

Thank you

Industry/Entity Type

It Company

Font styles to use
Other font styles liked:
• Maven Pro

Colors
ec1f27
0355a3
000000

Requirements
Must have
• Presentation template with Cover/Title Page, Bullets page and Regular page. Must match with our new logo.
• We would like the logo on the footer of the regular slides (not of course for the cover, dividers etc)
• Our logo colours are #b80016, #006ac6 and black
Nice to have
• Other type of slides, special bullets etc
Should not have
• I don't know

```html
<!DOCTYPE html>
<html lang="en">
<head>
<meta charset="utf-8">
<title>Copperline Ventures – Presentation Template</title>
<link href="https://fonts.googleapis.com/css2?family=Montserrat:wght@400;600;700;800&display=swap" rel="stylesheet">
<style>
:root{
  --red:#c8161e;
  --red-dark:#9c1016;
  --blue:#0355a3;
  --blue-light:#2d7fd0;
  --ink:#1e1e1e;
  --grey:#8a8a8a;
  --grey-light:#e9e9e9;
  --board:#e3e3e3;
}
*{box-sizing:border-box;margin:0;padding:0}
html,body{width:1200px;height:716px;overflow:hidden;background:var(--board)}
body{font-family:"Montserrat",Arial,sans-serif;color:var(--ink)}
.board{width:1200px;height:716px;display:grid;grid-template-columns:repeat(5,223px);grid-template-rows:repeat(5,128px);gap:11px 10px;padding:15px 18px}
.slide{position:relative;background:#fff;overflow:hidden;box-shadow:0 1px 2px rgba(0,0,0,.18)}
.abs{position:absolute}
.title{position:absolute;left:9px;top:8px;font-size:7px;font-weight:700;text-transform:uppercase;letter-spacing:.1px;color:var(--ink)}
.sub{position:absolute;left:9px;top:17px;font-size:3.6px;color:var(--grey)}
.brand{position:absolute;display:flex;align-items:center;gap:2px;font-weight:800;font-size:3.8px;line-height:1.05;text-transform:uppercase;color:var(--red)}
.brand i{display:block;width:6px;height:6px;background:var(--red)}
.brand.top{right:8px;top:7px}
.foot{position:absolute;left:0;right:0;bottom:0;height:2px;background:linear-gradient(90deg,var(--blue) 0 72%,var(--red) 72%)}
.foot-note{position:absolute;left:9px;bottom:4px;font-size:2.6px;color:var(--grey)}
.foot-mark{position:absolute;right:34px;bottom:3px;width:9px;height:4px;background:var(--blue)}
.foot-page{position:absolute;right:9px;bottom:4px;font-size:2.6px;color:var(--grey)}
.txt{font-size:3.4px;line-height:1.45;color:#555}
.red{color:var(--red)}
.blue{color:var(--blue)}
.h{font-size:4.4px;font-weight:700}
ul.bul{list-style:none}
ul.bul li{position:relative;padding-left:5px;margin-bottom:2px}
ul.bul li::before{content:"";position:absolute;left:0;top:1.3px;width:2px;height:2px;background:var(--red);border-radius:50%}
ul.bul li.sub2{padding-left:10px;color:#777}
ul.bul li.sub2::before{left:5px;background:var(--blue)}
.photo{position:absolute}
.dot{position:absolute;border-radius:50%}
.cover-title{font-weight:800;text-transform:uppercase}
/* table */
.tbl{position:absolute;left:9px;right:9px;top:28px;border-collapse:collapse;font-size:3px;width:205px}
.tbl th{color:#fff;font-weight:700;padding:2.5px 3px;text-align:left}
.tbl td{padding:2.6px 3px;color:#666}
.tbl tr:nth-child(even) td{background:var(--grey-light)}
.yr{display:flex;position:absolute;left:9px;right:9px;top:58px;height:7px}
.yr span{flex:1;font-size:3px;color:#fff;display:flex;align-items:center;justify-content:center;font-weight:700}
</style>
</head>
<body>
<main class="board">

<!-- Row 1 -->
<section class="slide cover-photo">
  <div class="photo" role="img" aria-label="Hands typing on a laptop, red toned" style="inset:0;background:linear-gradient(120deg,#d9d9dc 0%,#b7b9bf 40%,#d8484f 80%,#c8161e 100%)"></div>
  <div class="abs" style="left:0;top:34px;width:118px;height:32px;background:rgba(3,85,163,.85)"></div>
  <div class="abs cover-title" style="left:8px;top:40px;font-size:8px;color:#fff">Presentation Title</div>
  <div class="abs" style="left:8px;top:51px;font-size:4.5px;color:#fff;font-weight:600">Subtitle Goes Here</div>
  <div class="abs" style="left:8px;top:59px;font-size:2.8px;color:#e4ecf7">December, 2018</div>
  <div class="brand" style="left:8px;bottom:10px;color:#fff"><i style="background:#fff"></i>Copperline<br>Ventures</div>
</section>

<section class="slide cover-light">
  <div class="photo" role="img" aria-label="Faded office workspace" style="left:0;right:0;top:0;height:42px;background:linear-gradient(90deg,#f1f1f2,#e2e3e6)"></div>
  <div class="brand" style="left:10px;top:44px;font-size:5px"><i style="width:9px;height:9px"></i>Copperline<br>Ventures</div>
  <div class="abs cover-title red" style="left:10px;top:64px;font-size:8px">Presentation Title</div>
  <div class="abs" style="left:10px;top:75px;font-size:4.6px;font-weight:600">Subtitle Goes Here</div>
  <div class="abs" style="left:10px;top:84px;font-size:2.8px;color:var(--grey)">December, 2018</div>
</section>

<section class="slide cover-center">
  <div class="photo" role="img" aria-label="Faded desk with laptop" style="inset:0;background:linear-gradient(180deg,#efeff1,#e0e1e4)"></div>
  <div class="brand" style="left:0;right:0;top:38px;justify-content:center;font-size:5px"><i style="width:9px;height:9px"></i>Copperline<br>Ventures</div>
  <div class="abs cover-title red" style="left:0;right:0;top:60px;text-align:center;font-size:8px">Presentation Title</div>
  <div class="abs" style="left:0;right:0;top:71px;text-align:center;font-size:4.6px;font-weight:600">Subtitle Goes Here</div>
  <div class="abs" style="left:0;right:0;top:80px;text-align:center;font-size:2.8px;color:var(--grey)">December, 2018</div>
</section>

<section class="slide cover-band">
  <div class="photo" role="img" aria-label="Faded city workspace" style="inset:0;background:linear-gradient(180deg,#f3f3f4,#e6e7ea)"></div>
  <div class="abs cover-title red" style="left:10px;top:22px;font-size:8px">Presentation Title</div>
  <div class="abs" style="left:10px;top:33px;font-size:4.6px;font-weight:600">Subtitle Goes Here</div>
  <div class="abs" style="left:10px;top:41px;font-size:2.8px;color:var(--grey)">December, 2018</div>
  <div class="abs" style="left:0;top:90px;width:150px;height:20px;background:linear-gradient(90deg,var(--blue),var(--red))"></div>
  <div class="abs txt" style="left:10px;top:93px;width:130px;color:#fff;font-size:3px">Lorem ipsum dolor sit amet consectetur adipiscing elit sed do eiusmod tempor incididunt ut labore et dolore.</div>
  <div class="brand" style="left:158px;top:94px;font-size:4.5px"><i style="width:8px;height:8px"></i>Copperline<br>Ventures</div>
</section>

<section class="slide toc">
  <div class="title">Table of Content</div>
  <div class="sub">Subtitle Goes Here</div>
  <div class="brand top"><i></i>Copperline<br>Ventures</div>
  <div class="abs" style="left:30px;top:34px;width:170px;display:grid;grid-template-columns:1fr 1fr;gap:9px 14px">
    <div style="display:flex;gap:4px"><b style="background:var(--red);color:#fff;font-size:3.4px;width:9px;height:9px;display:flex;align-items:center;justify-content:center">01</b><div><div class="h red" style="font-size:3.4px">ABOUT US</div><div class="txt" style="font-size:2.6px">Lorem ipsum dolor sit amet</div></div></div>
    <div style="display:flex;gap:4px"><b style="background:var(--blue);color:#fff;font-size:3.4px;width:9px;height:9px;display:flex;align-items:center;justify-content:center">04</b><div><div class="h blue" style="font-size:3.4px">HOW WE DO</div><div class="txt" style="font-size:2.6px">Lorem ipsum dolor sit amet</div></div></div>
    <div style="display:flex;gap:4px"><b style="background:var(--blue);color:#fff;font-size:3.4px;width:9px;height:9px;display:flex;align-items:center;justify-content:center">02</b><div><div class="h blue" style="font-size:3.4px">OUR TEAM</div><div class="txt" style="font-size:2.6px">Lorem ipsum dolor sit amet</div></div></div>
    <div style="display:flex;gap:4px"><b style="background:var(--red);color:#fff;font-size:3.4px;width:9px;height:9px;display:flex;align-items:center;justify-content:center">05</b><div><div class="h red" style="font-size:3.4px">BUSINESS PROCESS</div><div class="txt" style="font-size:2.6px">Lorem ipsum dolor sit amet</div></div></div>
    <div style="display:flex;gap:4px"><b style="background:var(--red);color:#fff;font-size:3.4px;width:9px;height:9px;display:flex;align-items:center;justify-content:center">03</b><div><div class="h red" style="font-size:3.4px">WHAT WE DO</div><div class="txt" style="font-size:2.6px">Lorem ipsum dolor sit amet</div></div></div>
    <div style="display:flex;gap:4px"><b style="background:var(--blue);color:#fff;font-size:3.4px;width:9px;height:9px;display:flex;align-items:center;justify-content:center">06</b><div><div class="h blue" style="font-size:3.4px">CONTACT US</div><div class="txt" style="font-size:2.6px">Lorem ipsum dolor sit amet</div></div></div>
  </div>
  <div class="foot"></div>
</section>

<!-- Row 2 -->
<section class="slide one-col">
  <div class="title">One Column Sample</div>
  <div class="sub">Subtitle Goes Here</div>
  <div class="brand top"><i></i>Copperline<br>Ventures</div>
  <div class="abs" style="left:9px;top:28px;width:200px">
    <div class="h red" style="margin-bottom:2px">Lorem Ipsum</div>
    <ul class="bul txt">
      <li>Lorem ipsum dolor sit amet, consectetur adipiscing elit. Nullam posuere id nibh vitae.</li>
      <li class="sub2">Sed ut perspiciatis unde omnis iste natus error.</li>
      <li>Lorem ipsum dolor sit amet, consectetur adipiscing elit. Nullam posuere id nibh vitae.</li>
      <li class="sub2">Sed ut perspiciatis unde omnis iste natus error.</li>
      <li>Lorem ipsum dolor sit amet, consectetur adipiscing elit. Nullam posuere id nibh vitae.</li>
      <li class="sub2">Sed ut perspiciatis unde omnis iste natus error.</li>
    </ul>
  </div>
  <div class="foot-note">© 2018 Copperline Ventures. All rights reserved.</div><div class="foot-mark"></div><div class="foot-page">02</div>
  <div class="foot"></div>
</section>

<section class="slide two-col">
  <div class="title">Two Column Sample</div>
  <div class="sub">Subtitle Goes Here</div>
  <div class="brand top"><i></i>Copperline<br>Ventures</div>
  <div class="abs" style="left:9px;top:28px;width:96px">
    <div class="h red" style="margin-bottom:2px">Lorem Ipsum</div>
    <ul class="bul txt">
      <li>Lorem ipsum dolor sit amet, consectetur adipiscing elit nullam.</li>
      <li class="sub2">Sed ut perspiciatis unde omnis.</li>
      <li>Lorem ipsum dolor sit amet, consectetur adipiscing elit nullam.</li>
      <li class="sub2">Sed ut perspiciatis unde omnis.</li>
      <li>Lorem ipsum dolor sit amet, consectetur adipiscing elit.</li>
    </ul>
  </div>
  <div class="abs" style="left:116px;top:28px;width:96px">
    <div class="h red" style="margin-bottom:2px">Lorem Ipsum</div>
    <ul class="bul txt">
      <li>Lorem ipsum dolor sit amet, consectetur adipiscing elit nullam.</li>
      <li class="sub2">Sed ut perspiciatis unde omnis.</li>
      <li>Lorem ipsum dolor sit amet, consectetur adipiscing elit nullam.</li>
      <li class="sub2">Sed ut perspiciatis unde omnis.</li>
      <li>Lorem ipsum dolor sit amet, consectetur adipiscing elit.</li>
    </ul>
  </div>
  <div class="foot-note">© 2018 Copperline Ventures. All rights reserved.</div><div class="foot-mark"></div><div class="foot-page">03</div>
  <div class="foot"></div>
</section>

<section class="slide right-col">
  <div class="title">Right Column</div>
  <div class="sub">Subtitle Goes Here</div>
  <div class="brand top"><i></i>Copperline<br>Ventures</div>
  <div class="abs" style="left:9px;top:28px;width:100px">
    <ul class="bul txt">
      <li>Lorem ipsum dolor sit amet, consectetur adipiscing elit nullam.</li>
      <li class="sub2">Sed ut perspiciatis unde omnis.</li>
      <li>Lorem ipsum dolor sit amet, consectetur adipiscing elit nullam.</li>
      <li class="sub2">Sed ut perspiciatis unde omnis.</li>
      <li>Lorem ipsum dolor sit amet, consectetur adipiscing elit nullam.</li>
      <li class="sub2">Sed ut perspiciatis unde omnis.</li>
    </ul>
  </div>
  <svg class="abs" style="left:125px;top:28px" width="80" height="70" viewBox="0 0 80 70" aria-label="Pyramid diagram">
    <polygon points="40,2 50,18 30,18" fill="var(--red)"/>
    <polygon points="29,20 51,20 61,36 19,36" fill="var(--blue)"/>
    <polygon points="18,38 62,38 72,54 8,54" fill="#2e6fb7"/>
    <polygon points="7,56 73,56 80,68 0,68" fill="#4a4a4a"/>
  </svg>
  <div class="foot-note">© 2018 Copperline Ventures. All rights reserved.</div><div class="foot-mark"></div><div class="foot-page">04</div>
  <div class="foot"></div>
</section>

<section class="slide table-sample">
  <div class="title">Table Sample</div>
  <div class="sub">Subtitle Goes Here</div>
  <div class="brand top"><i></i>Copperline<br>Ventures</div>
  <table class="tbl">
    <tr><th style="background:var(--red)">Lorem Ipsum</th><th style="background:var(--blue)">Lorem Ipsum 1</th><th style="background:var(--red)">Lorem Ipsum 1</th><th style="background:var(--blue)">Lorem Ipsum 2</th><th style="background:var(--red)">Lorem Ipsum 3</th></tr>
    <tr><td>Lorem ipsum</td><td>Dolor sit</td><td>Dolor sit</td><td>Dolor sit</td><td>Dolor sit</td></tr>
    <tr><td>Lorem ipsum</td><td>Dolor sit</td><td>Dolor sit</td><td>Dolor sit</td><td>Dolor sit</td></tr>
    <tr><td>Lorem ipsum</td><td>Dolor sit</td><td>Dolor sit</td><td>Dolor sit</td><td>Dolor sit</td></tr>
    <tr><td>Lorem ipsum</td><td>Dolor sit</td><td>Dolor sit</td><td>Dolor sit</td><td>Dolor sit</td></tr>
    <tr><td>Lorem ipsum</td><td>Dolor sit</td><td>Dolor sit</td><td>Dolor sit</td><td>Dolor sit</td></tr>
    <tr><td>Lorem ipsum</td><td>Dolor sit</td><td>Dolor sit</td><td>Dolor sit</td><td>Dolor sit</td></tr>
  </table>
  <div class="foot-note">© 2018 Copperline Ventures. All rights reserved.</div><div class="foot-mark"></div><div class="foot-page">05</div>
  <div class="foot"></div>
</section>

<section class="slide icons-content">
  <div class="title">Content with Icons</div>
  <div class="sub">Subtitle Goes Here</div>
  <div class="brand top"><i></i>Copperline<br>Ventures</div>
  <div class="photo" role="img" aria-label="Presenter speaking in a bright office" style="left:0;right:0;top:26px;height:42px;background:linear-gradient(90deg,#8f2a31,#b95a5e 40%,#c7cbd3 80%,#8aa0bc)"></div>
  <div class="dot" style="left:23px;top:62px;width:11px;height:11px;background:var(--red);border:1.5px solid #fff"></div>
  <div class="dot" style="left:74px;top:62px;width:11px;height:11px;background:var(--blue);border:1.5px solid #fff"></div>
  <div class="dot" style="left:125px;top:62px;width:11px;height:11px;background:var(--red);border:1.5px solid #fff"></div>
  <div class="dot" style="left:176px;top:62px;width:11px;height:11px;background:var(--blue);border:1.5px solid #fff"></div>
  <div class="abs" style="left:10px;top:78px;width:205px;display:grid;grid-template-columns:repeat(4,1fr);gap:4px">
    <div><div class="h" style="font-size:3.4px">Lorem Ipsum</div><div class="txt" style="font-size:2.6px">Dolor sit amet consectetur elit sed do</div></div>
    <div><div class="h" style="font-size:3.4px">Lorem Ipsum</div><div class="txt" style="font-size:2.6px">Dolor sit amet consectetur elit sed do</div></div>
    <div><div class="h" style="font-size:3.4px">Lorem Ipsum</div><div class="txt" style="font-size:2.6px">Dolor sit amet consectetur elit sed do</div></div>
    <div><div class="h" style="font-size:3.4px">Lorem Ipsum</div><div class="txt" style="font-size:2.6px">Dolor sit amet consectetur elit sed do</div></div>
  </div>
  <div class="foot"></div>
</section>

<!-- Row 3 -->
<section class="slide icons-list">
  <div class="title">Icons List Sample</div>
  <div class="sub">Subtitle Goes Here</div>
  <div class="brand top"><i></i>Copperline<br>Ventures</div>
  <div class="abs" style="left:14px;top:32px;width:200px;display:grid;grid-template-columns:repeat(3,1fr);gap:12px 6px">
    <div style="display:flex;gap:4px"><svg width="10" height="9"><rect x="1" y="4" width="2" height="5" fill="var(--red)"/><rect x="4" y="2" width="2" height="7" fill="var(--blue)"/><rect x="7" y="0" width="2" height="9" fill="var(--red)"/></svg><div><div class="h" style="font-size:3.2px">BUSINESS 1</div><div class="txt" style="font-size:2.5px">Lorem ipsum dolor sit amet elit</div></div></div>
    <div style="display:flex;gap:4px"><svg width="10" height="9"><rect x="0.5" y="0.5" width="9" height="6" fill="none" stroke="var(--blue)"/><rect x="3" y="7" width="4" height="2" fill="var(--red)"/></svg><div><div class="h" style="font-size:3.2px">BUSINESS 2</div><div class="txt" style="font-size:2.5px">Lorem ipsum dolor sit amet elit</div></div></div>
    <div style="display:flex;gap:4px"><svg width="10" height="9"><circle cx="5" cy="4" r="3.5" fill="none" stroke="var(--red)"/><rect x="4" y="7" width="2" height="2" fill="var(--blue)"/></svg><div><div class="h" style="font-size:3.2px">BUSINESS 3</div><div class="txt" style="font-size:2.5px">Lorem ipsum dolor sit amet elit</div></div></div>
    <div style="display:flex;gap:4px"><svg width="10" height="9"><rect x="3.5" y="0" width="3" height="3" fill="var(--blue)"/><rect x="0" y="6" width="3" height="3" fill="var(--red)"/><rect x="7" y="6" width="3" height="3" fill="var(--red)"/><path d="M5 3v2M1.5 6V5h7v1" stroke="#555" stroke-width=".6" fill="none"/></svg><div><div class="h" style="font-size:3.2px">BUSINESS 4</div><div class="txt" style="font-size:2.5px">Lorem ipsum dolor sit amet elit</div></div></div>
    <div style="display:flex;gap:4px"><svg width="10" height="9"><rect x="0.5" y="0.5" width="9" height="7" fill="none" stroke="var(--red)"/><path d="M2 6l2-2 2 1 2-3" stroke="var(--blue)" stroke-width=".8" fill="none"/></svg><div><div class="h" style="font-size:3.2px">BUSINESS 5</div><div class="txt" style="font-size:2.5px">Lorem ipsum dolor sit amet elit</div></div></div>
    <div style="display:flex;gap:4px"><svg width="10" height="9"><rect x="0.5" y="2" width="9" height="6" fill="none" stroke="var(--blue)"/><path d="M1 2l4 3 4-3" stroke="var(--red)" stroke-width=".8" fill="none"/></svg><div><div class="h" style="font-size:3.2px">BUSINESS 6</div><div class="txt" style="font-size:2.5px">Lorem ipsum dolor sit amet elit</div></div></div>
  </div>
  <div class="foot-note">© 2018 Copperline Ventures. All rights reserved.</div><div class="foot-mark"></div><div class="foot-page">07</div>
  <div class="foot"></div>
</section>

<section class="slide about-me">
  <div class="title">About Me</div>
  <div class="brand top"><i></i>Copperline<br>Ventures</div>
  <div class="photo" role="img" aria-label="Portrait of a team member" style="left:0;top:24px;width:85px;height:92px;background:linear-gradient(180deg,#d7d7d7,#9a9a9a)"></div>
  <svg class="abs" style="left:78px;top:24px" width="14" height="92" aria-hidden="true"><path d="M12 0L2 92" stroke="var(--red)" stroke-width="1.5"/><path d="M14 10L6 92" stroke="var(--blue)" stroke-width="1"/></svg>
  <div class="abs txt" style="left:98px;top:26px;width:115px">
    <p style="margin-bottom:3px">Lorem ipsum dolor sit amet, consectetur adipiscing elit. Nullam posuere id nibh vitae lacinia. Morbi eget urna sit amet dui mattis cursus.</p>
    <p style="margin-bottom:3px">Sed ut perspiciatis unde omnis iste natus error sit voluptatem accusantium doloremque laudantium totam rem aperiam.</p>
    <p>Quis autem vel eum iure reprehenderit qui in ea voluptate velit esse.</p>
    <div class="h red" style="margin-top:3px">JOHN DOE</div>
    <div style="font-size:2.8px">Director &amp; CEO</div>
  </div>
  <div class="foot"></div>
</section>

<section class="slide pie-chart">
  <div class="title">Pie Chart Sample</div>
  <div class="sub">Subtitle Goes Here</div>
  <div class="brand top"><i></i>Copperline<br>Ventures</div>
  <div class="abs h" style="left:0;right:0;top:27px;text-align:center;font-size:4.2px">Lorem ipsum dolor sit amet</div>
  <svg class="abs" style="left:80px;top:35px" width="60" height="60" viewBox="-30 -30 60 60" aria-label="Pie chart: 58%, 19%, 13%, 9%">
    <g transform="rotate(-90)">
      <circle r="14" fill="none" stroke="var(--red)" stroke-width="28" stroke-dasharray="51 88"/>
      <circle r="14" fill="none" stroke="#c9c9c9" stroke-width="28" stroke-dasharray="0 51 16.7 88"/>
      <circle r="14" fill="none" stroke="var(--blue)" stroke-width="28" stroke-dasharray="0 67.7 11.4 88"/>
      <circle r="14" fill="none" stroke="#7fa9d6" stroke-width="28" stroke-dasharray="0 79.1 8.9 88"/>
    </g>
    <text x="12" y="3" font-size="5" fill="#fff" font-weight="700">58%</text>
    <text x="-18" y="9" font-size="4" fill="#fff" font-weight="700">13%</text>
    <text x="-12" y="-9" font-size="4" fill="#333" font-weight="700">19%</text>
  </svg>
  <div class="abs txt" style="left:22px;top:40px;font-size:2.6px"><b class="blue">Solutions</b><br>Lorem ipsum</div>
  <div class="abs txt" style="left:40px;top:56px;font-size:2.6px"><b class="red">Business Plan</b><br>Lorem ipsum</div>
  <div class="abs txt" style="left:30px;top:76px;font-size:2.6px"><b class="red">Support</b><br>Lorem ipsum</div>
  <div class="abs txt" style="left:150px;top:58px;font-size:2.6px"><b class="red">Executive Management</b><br>Lorem ipsum dolor</div>
  <div class="abs txt" style="left:82px;top:98px;font-size:2.6px">■ Lorem ipsum &nbsp; ■ Dolor sit &nbsp; ■ Amet</div>
  <div class="foot"></div>
</section>

<section class="slide bar-chart">
  <div class="title">Bar Chart Sample</div>
  <div class="sub">Subtitle Goes Here</div>
  <div class="brand top"><i></i>Copperline<br>Ventures</div>
  <div class="abs h" style="left:0;right:0;top:27px;text-align:center;font-size:4.2px">Lorem ipsum dolor sit amet</div>
  <svg class="abs" style="left:12px;top:36px" width="200" height="70" viewBox="0 0 200 70" aria-label="Bar chart with eight categories">
    <g stroke="#ececec" stroke-width=".5"><path d="M8 5H198M8 20H198M8 35H198M8 50H198M8 62H198"/></g>
    <g font-size="3" fill="#999"><text x="0" y="6">50</text><text x="0" y="21">40</text><text x="0" y="36">30</text><text x="0" y="51">20</text><text x="0" y="63">0</text></g>
    <g fill="var(--red)"><rect x="16" y="25" width="6" height="37"/><rect x="40" y="34" width="6" height="28"/><rect x="64" y="28" width="6" height="34"/><rect x="88" y="20" width="6" height="42"/><rect x="112" y="32" width="6" height="30"/><rect x="136" y="8" width="6" height="54"/><rect x="160" y="30" width="6" height="32"/><rect x="184" y="24" width="6" height="38"/></g>
    <g fill="var(--blue)"><rect x="23" y="38" width="6" height="24"/><rect x="47" y="30" width="6" height="32"/><rect x="71" y="16" width="6" height="46"/><rect x="95" y="33" width="6" height="29"/><rect x="119" y="28" width="6" height="34"/><rect x="143" y="35" width="6" height="27"/><rect x="167" y="27" width="6" height="35"/><rect x="191" y="32" width="6" height="30"/></g>
    <g font-size="2.6" fill="#999"><text x="15" y="68">Cat 1</text><text x="39" y="68">Cat 2</text><text x="63" y="68">Cat 3</text><text x="87" y="68">Cat 4</text><text x="111" y="68">Cat 5</text><text x="135" y="68">Cat 6</text><text x="159" y="68">Cat 7</text><text x="183" y="68">Cat 8</text></g>
  </svg>
  <div class="foot"></div>
</section>

<section class="slide bar-chart-3d">
  <div class="title">3D Bar Chart Sample</div>
  <div class="sub">Subtitle Goes Here</div>
  <div class="brand top"><i></i>Copperline<br>Ventures</div>
  <div class="abs h" style="left:0;right:0;top:27px;text-align:center;font-size:4.2px">Lorem ipsum dolor sit amet</div>
  <svg class="abs" style="left:12px;top:36px" width="200" height="70" viewBox="0 0 200 70" aria-label="3D bar chart with eight categories">
    <g stroke="#ececec" stroke-width=".5"><path d="M8 5H198M8 20H198M8 35H198M8 50H198M8 62H198"/></g>
    <g fill="var(--red)"><rect x="16" y="25" width="6" height="37"/><rect x="40" y="34" width="6" height="28"/><rect x="64" y="28" width="6" height="34"/><rect x="88" y="20" width="6" height="42"/><rect x="112" y="32" width="6" height="30"/><rect x="136" y="8" width="6" height="54"/><rect x="160" y="30" width="6" height="32"/><rect x="184" y="24" width="6" height="38"/></g>
    <g fill="var(--red-dark)"><rect x="22" y="26" width="1.5" height="36"/><rect x="46" y="35" width="1.5" height="27"/><rect x="70" y="29" width="1.5" height="33"/><rect x="94" y="21" width="1.5" height="41"/><rect x="118" y="33" width="1.5" height="29"/><rect x="142" y="9" width="1.5" height="53"/><rect x="166" y="31" width="1.5" height="31"/><rect x="190" y="25" width="1.5" height="37"/></g>
    <g fill="var(--blue)"><rect x="24" y="38" width="6" height="24"/><rect x="48" y="30" width="6" height="32"/><rect x="72" y="16" width="6" height="46"/><rect x="96" y="33" width="6" height="29"/><rect x="120" y="28" width="6" height="34"/><rect x="144" y="35" width="6" height="27"/><rect x="168" y="27" width="6" height="35"/><rect x="192" y="32" width="6" height="30"/></g>
    <g font-size="2.6" fill="#999"><text x="15" y="68">Cat 1</text><text x="39" y="68">Cat 2</text><text x="63" y="68">Cat 3</text><text x="87" y="68">Cat 4</text><text x="111" y="68">Cat 5</text><text x="135" y="68">Cat 6</text><text x="159" y="68">Cat 7</text><text x="183" y="68">Cat 8</text></g>
  </svg>
  <div class="foot"></div>
</section>

<!-- Row 4 -->
<section class="slide team">
  <div class="title">Team Sample</div>
  <div class="sub">Subtitle Goes Here</div>
  <div class="brand top"><i></i>Copperline<br>Ventures</div>
  <div class="abs" style="left:14px;top:32px;width:196px;display:grid;grid-template-columns:repeat(4,1fr);text-align:center">
    <div><div role="img" aria-label="Team member portrait" style="width:26px;height:26px;margin:0 auto;border-radius:50%;background:#b9b9b9;border:1.5px solid var(--red)"></div><div class="h red" style="font-size:3.4px;margin-top:4px">JOHN DOE</div><div style="font-size:2.6px">Director &amp; CEO</div><div class="txt" style="font-size:2.4px">Lorem ipsum dolor sit</div></div>
    <div><div role="img" aria-label="Team member portrait" style="width:26px;height:26px;margin:0 auto;border-radius:50%;background:#b9b9b9;border:1.5px solid var(--red)"></div><div class="h red" style="font-size:3.4px;margin-top:4px">JOHN DOE</div><div style="font-size:2.6px">Director &amp; CEO</div><div class="txt" style="font-size:2.4px">Lorem ipsum dolor sit</div></div>
    <div><div role="img" aria-label="Team member portrait" style="width:26px;height:26px;margin:0 auto;border-radius:50%;background:#b9b9b9;border:1.5px solid var(--red)"></div><div class="h red" style="font-size:3.4px;margin-top:4px">JOHN DOE</div><div style="font-size:2.6px">Director &amp; CEO</div><div class="txt" style="font-size:2.4px">Lorem ipsum dolor sit</div></div>
    <div><div role="img" aria-label="Team member portrait" style="width:26px;height:26px;margin:0 auto;border-radius:50%;background:#b9b9b9;border:1.5px solid var(--red)"></div><div class="h red" style="font-size:3.4px;margin-top:4px">JOHN DOE</div><div style="font-size:2.6px">Director &amp; CEO</div><div class="txt" style="font-size:2.4px">Lorem ipsum dolor sit</div></div>
  </div>
  <div class="foot"></div>
</section>

<section class="slide timeline">
  <div class="title">Timeline Sample</div>
  <div class="sub">Subtitle Goes Here</div>
  <div class="brand top"><i></i>Copperline<br>Ventures</div>
  <div class="abs" style="left:9px;top:28px;width:205px;display:grid;grid-template-columns:repeat(4,1fr);gap:4px">
    <div class="txt" style="font-size:2.5px"><b style="color:#222">Description 1</b><br>Lorem ipsum dolor sit amet elit</div>
    <div class="txt" style="font-size:2.5px"><b style="color:#222">Description 3</b><br>Lorem ipsum dolor sit amet elit</div>
    <div class="txt" style="font-size:2.5px"><b style="color:#222">Description 5</b><br>Lorem ipsum dolor sit amet elit</div>
    <div class="txt" style="font-size:2.5px"><b style="color:#222">Description 7</b><br>Lorem ipsum dolor sit amet elit</div>
  </div>
  <div class="yr"><span style="background:#bdbdbd">2010</span><span style="background:var(--red)">2011</span><span style="background:#bdbdbd">2012</span><span style="background:var(--blue)">2013</span><span style="background:#bdbdbd">2014</span><span style="background:#111">2015</span><span style="background:#bdbdbd">2016</span><span style="background:var(--red)">2017</span></div>
  <div class="abs" style="left:35px;top:72px;width:180px;display:grid;grid-template-columns:repeat(3,1fr);gap:4px">
    <div class="txt" style="font-size:2.5px"><b style="color:#222">Description 2</b><br>Lorem ipsum dolor sit amet elit</div>
    <div class="txt" style="font-size:2.5px"><b style="color:#222">Description 4</b><br>Lorem ipsum dolor sit amet elit</div>
    <div class="txt" style="font-size:2.5px"><b style="color:#222">Description 6</b><br>Lorem ipsum dolor sit amet elit</div>
  </div>
  <div class="foot"></div>
</section>

<section class="slide plan">
  <div class="title">Plan Sample</div>
  <div class="sub">Subtitle Goes Here</div>
  <div class="brand top"><i></i>Copperline<br>Ventures</div>
  <div class="abs" style="left:30px;top:28px;width:165px;display:grid;grid-template-columns:repeat(3,1fr);gap:6px;text-align:center">
    <div><div role="img" aria-label="City skyline photo" style="height:34px;background:linear-gradient(180deg,#8fb3d9,#3b6aa0)"></div><div class="h red" style="font-size:3.4px;margin-top:4px">PLAN 1</div><div class="txt" style="font-size:2.5px">Lorem ipsum dolor sit amet consectetur</div></div>
    <div><div role="img" aria-label="Team meeting photo" style="height:34px;background:linear-gradient(180deg,#d9c7a8,#8a7656)"></div><div class="h red" style="font-size:3.4px;margin-top:4px">PLAN 2</div><div class="txt" style="font-size:2.5px">Lorem ipsum dolor sit amet consectetur</div></div>
    <div><div role="img" aria-label="People celebrating at sunset" style="height:34px;background:linear-gradient(180deg,#9fd0e6,#2f5f86)"></div><div class="h red" style="font-size:3.4px;margin-top:4px">PLAN 3</div><div class="txt" style="font-size:2.5px">Lorem ipsum dolor sit amet consectetur</div></div>
  </div>
  <div class="foot"></div>
</section>

<section class="slide graphic">
  <div class="title">Graphic Sample</div>
  <div class="sub">Subtitle Goes Here</div>
  <div class="brand top"><i></i>Copperline<br>Ventures</div>
  <svg class="abs" style="left:86px;top:30px" width="52" height="70" viewBox="0 0 52 70" aria-label="Circular diagram with six points">
    <circle cx="26" cy="35" r="20" fill="none" stroke="#dcdcdc" stroke-width="1"/>
    <circle cx="26" cy="35" r="9" fill="none" stroke="var(--red)" stroke-width="1.5"/>
    <g fill="#fff" stroke="var(--red)" stroke-width=".8"><circle cx="26" cy="15" r="3.5"/><circle cx="43" cy="25" r="3.5"/><circle cx="43" cy="45" r="3.5"/><circle cx="26" cy="55" r="3.5"/><circle cx="9" cy="45" r="3.5"/><circle cx="9" cy="25" r="3.5"/></g>
  </svg>
  <div class="abs txt" style="left:12px;top:36px;width:68px;text-align:right;font-size:2.6px">Lorem ipsum dolor sit amet, consectetur adipiscing elit<br><br>Lorem ipsum dolor sit amet, consectetur adipiscing elit<br><br>Lorem ipsum dolor sit amet, consectetur adipiscing elit</div>
  <div class="abs txt" style="left:144px;top:36px;width:68px;font-size:2.6px">Lorem ipsum dolor sit amet, consectetur adipiscing elit<br><br>Lorem ipsum dolor sit amet, consectetur adipiscing elit<br><br>Lorem ipsum dolor sit amet, consectetur adipiscing elit</div>
  <div class="foot"></div>
</section>

<section class="slide section-break">
  <div class="photo" role="img" aria-label="Colleagues working at a table" style="inset:0;background:linear-gradient(135deg,#8b7f78,#4f4a48 60%,#6b6562)"></div>
  <div class="abs" style="left:0;right:0;top:74px;height:28px;background:rgba(120,120,120,.85)"></div>
  <div class="abs" style="left:8px;top:80px;font-size:7px;font-weight:700;color:#fff">Section Break</div>
  <div class="abs" style="left:8px;top:90px;font-size:3.4px;color:#eee">About Us, Who We are</div>
  <div class="dot" style="left:150px;top:78px;width:20px;height:20px;background:#fff"></div>
  <svg class="abs" style="left:155px;top:84px" width="10" height="8" aria-hidden="true"><rect x="0" y="0" width="6" height="4" rx="1" fill="#888"/><rect x="4" y="3" width="6" height="4" rx="1" fill="#bbb"/></svg>
</section>

<!-- Row 5 -->
<section class="slide process">
  <div class="title">Graphic Process Sample</div>
  <div class="sub">Subtitle Goes Here</div>
  <div class="brand top"><i></i>Copperline<br>Ventures</div>
  <svg class="abs" style="left:82px;top:28px" width="60" height="60" viewBox="-30 -30 60 60" aria-label="Six step circular process">
    <g transform="rotate(-90)" fill="none" stroke-width="11">
      <circle r="20" stroke="var(--blue)" stroke-dasharray="62.8 125.6" transform="rotate(180)"/>
      <circle r="20" stroke="var(--red-dark)" stroke-dasharray="62.8 125.6"/>
      <circle r="20" stroke="#fff" stroke-width="12" stroke-dasharray="1.5 19.4"/>
    </g>
  </svg>
  <div class="abs txt" style="left:10px;top:36px;width:66px;text-align:right;font-size:2.6px">Lorem ipsum dolor sit amet, consectetur adipiscing elit<br><br>Lorem ipsum dolor sit amet, consectetur adipiscing elit<br><br>Lorem ipsum dolor sit amet, consectetur adipiscing elit</div>
  <div class="abs txt" style="left:148px;top:36px;width:66px;font-size:2.6px">Lorem ipsum dolor sit amet, consectetur adipiscing elit<br><br>Lorem ipsum dolor sit amet, consectetur adipiscing elit<br><br>Lorem ipsum dolor sit amet, consectetur adipiscing elit</div>
  <div class="foot"></div>
</section>

<section class="slide process">
  <div class="title">Graphic Process Sample</div>
  <div class="sub">Subtitle Goes Here</div>
  <div class="brand top"><i></i>Copperline<br>Ventures</div>
  <svg class="abs" style="left:82px;top:28px" width="60" height="60" viewBox="-30 -30 60 60" aria-label="Six step circular process">
    <g transform="rotate(-90)" fill="none" stroke-width="11">
      <circle r="20" stroke="var(--blue)" stroke-dasharray="62.8 125.6" transform="rotate(180)"/>
      <circle r="20" stroke="var(--red-dark)" stroke-dasharray="62.8 125.6"/>
      <circle r="20" stroke="#fff" stroke-width="12" stroke-dasharray="1.5 19.4"/>
    </g>
  </svg>
  <div class="abs txt" style="left:10px;top:36px;width:66px;text-align:right;font-size:2.6px">Lorem ipsum dolor sit amet, consectetur adipiscing elit<br><br>Lorem ipsum dolor sit amet, consectetur adipiscing elit<br><br>Lorem ipsum dolor sit amet, consectetur adipiscing elit</div>
  <div class="abs txt" style="left:148px;top:36px;width:66px;font-size:2.6px">Lorem ipsum dolor sit amet, consectetur adipiscing elit<br><br>Lorem ipsum dolor sit amet, consectetur adipiscing elit<br><br>Lorem ipsum dolor sit amet, consectetur adipiscing elit</div>
  <div class="foot"></div>
</section>

<section class="slide testimonial">
  <div class="title">Testimonial Sample</div>
  <div class="sub">Subtitle Goes Here</div>
  <div class="brand top"><i></i>Copperline<br>Ventures</div>
  <div class="dot" role="img" aria-label="Client portrait" style="left:101px;top:24px;width:20px;height:20px;background:#bdbdbd;border:1.5px solid var(--red)"></div>
  <div class="abs h red" style="left:0;right:0;top:47px;text-align:center;font-size:3.4px">JOHN DOE</div>
  <div class="abs txt" style="left:50px;width:123px;top:52px;text-align:center;font-size:2.6px">Lorem ipsum dolor sit amet, consectetur adipiscing elit. Nullam posuere id nibh vitae lacinia morbi eget.</div>
  <div class="abs" style="left:0;right:0;top:72px;height:52px;background:#e7e7e7"></div>
  <div class="abs" style="left:16px;top:78px;width:190px;display:grid;grid-template-columns:repeat(4,1fr);text-align:center">
    <div><div class="dot" style="position:static;width:10px;height:10px;margin:0 auto;background:var(--red)"></div><div class="h" style="font-size:3px;margin-top:2px">Testimonial 1</div><div class="txt" style="font-size:2.4px">Lorem ipsum dolor sit</div></div>
    <div><div class="dot" style="position:static;width:10px;height:10px;margin:0 auto;background:var(--blue)"></div><div class="h" style="font-size:3px;margin-top:2px">Testimonial 2</div><div class="txt" style="font-size:2.4px">Lorem ipsum dolor sit</div></div>
    <div><div class="dot" style="position:static;width:10px;height:10px;margin:0 auto;background:var(--red)"></div><div class="h" style="font-size:3px;margin-top:2px">Testimonial 3</div><div class="txt" style="font-size:2.4px">Lorem ipsum dolor sit</div></div>
    <div><div class="dot" style="position:static;width:10px;height:10px;margin:0 auto;background:var(--blue)"></div><div class="h" style="font-size:3px;margin-top:2px">Testimonial 4</div><div class="txt" style="font-size:2.4px">Lorem ipsum dolor sit</div></div>
  </div>
  <div class="foot"></div>
</section>

<section class="slide map">
  <div class="title">Map Sample</div>
  <div class="sub">Subtitle Goes Here</div>
  <div class="brand top"><i></i>Copperline<br>Ventures</div>
  <div class="photo" role="img" aria-label="World map" style="left:30px;top:28px;width:165px;height:78px;background:radial-gradient(ellipse at 50% 50%,#cfcfcf 0%,#e2e2e2 60%,#fff 100%)"></div>
  <div class="abs" style="left:12px;top:44px;text-align:right;font-size:3px;line-height:1.1">North<br>America<br><b class="red" style="font-size:6px">63%</b></div>
  <div class="abs" style="left:38px;top:76px;text-align:right;font-size:3px;line-height:1.1">South<br>America<br><b class="blue" style="font-size:6px">89%</b></div>
  <div class="abs" style="left:108px;top:80px;font-size:3px;line-height:1.1">Africa<br><b class="blue" style="font-size:6px">50%</b></div>
  <div class="abs" style="left:172px;top:44px;font-size:3px;line-height:1.1">Asia<br><b class="blue" style="font-size:6px">79%</b></div>
  <div class="abs" style="left:166px;top:80px;font-size:3px;line-height:1.1">Australia<br><b style="font-size:6px;color:#e58a1a">86%</b></div>
  <div class="foot"></div>
</section>

<section class="slide thank-you">
  <div class="brand" style="left:12px;top:14px;font-size:5px"><i style="width:9px;height:9px"></i>Copperline<br>Ventures</div>
  <div class="abs" style="left:12px;top:38px;font-size:9px;font-weight:800">THANK YOU</div>
  <div class="abs" style="left:12px;top:54px;font-size:2.8px;line-height:1.35">
    <div><b class="red">● ADDRESS</b><br>&nbsp;&nbsp;&nbsp;48 Harbor Lane, Riverton</div>
    <div style="margin-top:2px"><b class="red">● EMAIL</b><br>&nbsp;&nbsp;&nbsp;hello@copperline.example</div>
    <div style="margin-top:2px"><b class="red">● PHONE</b><br>&nbsp;&nbsp;&nbsp;+1 555 014 2290</div>
    <div style="margin-top:2px"><b class="red">● WEB</b><br>&nbsp;&nbsp;&nbsp;copperline.example</div>
  </div>
  <div class="photo" role="img" aria-label="Glass office towers seen from below" style="left:105px;top:0;right:0;bottom:0;background:linear-gradient(160deg,#2c4c78,#6b86ad 50%,#1c2f4d)"></div>
  <svg class="abs" style="left:105px;top:0" width="118" height="128" aria-hidden="true"><polygon points="0,0 24,0 0,128" fill="#fff"/><path d="M24 0L0 128" stroke="var(--red)" stroke-width="2"/></svg>
</section>

</main>
</body>
</html>
```